Rest. Build. Thrive. Book Cover

I would like a book cover for the print edition book I am self publishing. My cover will require front, back, and spine design. I have provided a template to assist with sizing and spacing.

My book is named "Rest. Build. Thrive. A Hands-On Diet, Drive to Act, and Attitude Handbook Building Energy Toward Stronger Vitality and Balance" by Gregory Halvorsen RD, CPT. I use the concept of waves as an analogy for forward progress in life and would like that reflected in the cover design. I would like the color scheme to be blacks, whites, grey, and various shades of blue. I have provided a style guide for reference. Please include my logo on the front, spine, and back of the design. Please include an about the author, book summary, and my picture on the back. I have provided the wording below.

About the Author: Gregory Halvorsen is a Registered Dietitian and Certified Personal Trainer from Cleveland, OH. He graduated from the Westbrook Valley University and currently works as a health coach in the healthcare industry. His passions are fitness, nutrition, science, and motivation. He has extensive knowledge and experience in wellness, healthcare, and disease treatment and disease. Gregory has worked with hundreds of people through counseling, consulting, and coaching in an effort to make a difference in their long-term health. In his spare time, he enjoys exercising, watching movies, and trying out new foods.

Book Summary: Believe in you. Trust in You. Rest. Build. Thrive. is a book committed to you. Behavior change and improved health can be challenging. You must feel empowered to make decisions and changes create momentum in the right direction. But, you may not always have the knowledge to do that. This book provides you with practical and fun tools and tips to improve your nutrition, motivation to move, and mindset. You are awesome. You are beautiful. You have the power to control your destiny and future. All you have to do is Rest, Build, and Thrive!

Please use a modern/ futuristic font style for the title. I have also provided some draft book covers for inspiration/ direction. Thank you!

Colors

Designer to choose only greyscale colors for use in the design.

Requirements
Must have
• Color scheme, about author, profile picture, and book summary on back, wave themed graphics

```html
<!DOCTYPE html>
<html lang="en">
<head>
<meta charset="utf-8">
<title>Rest. Build. Thrive. – Book Cover</title>
<link rel="stylesheet" href="https://fonts.googleapis.com/css2?family=Arimo:wght@400&family=Lobster&display=swap">
<style>
  :root {
    --back-grey: #b3b5b4;
    --spine-dark: #2a2826;
    --navy: #293642;
    --cream: #fdf8dc;
    --ink: #2e2e2e;
    --brand-blue: #3592b8;
    --wave-light: rgba(255, 255, 255, 0.55);
    --wave-blue: rgba(53, 146, 184, 0.55);
    --frame: #3a3a3a;
  }
  * { margin: 0; padding: 0; box-sizing: border-box; }
  html, body { width: 1200px; height: 906px; overflow: hidden; background: var(--back-grey); }
  .cover { position: relative; width: 1200px; height: 906px; font-family: "Arimo", Arial, sans-serif; color: var(--ink); }

  .back-cover { position: absolute; left: 0; top: 0; width: 563px; height: 906px; background: var(--back-grey); }
  .section-heading { position: absolute; left: 60px; font-family: "Lobster", cursive; font-weight: 400; font-size: 29px; color: #2b2b2b; }
  .summary-heading { top: 86px; }
  .author-heading { top: 327px; }
  .summary-text { position: absolute; left: 61px; top: 132px; width: 414px; font-size: 13.4px; line-height: 15.35px; text-align: justify; }
  .author-block { position: absolute; left: 61px; top: 322px; width: 414px; font-size: 13.4px; line-height: 15.35px; }
  .author-photo { float: right; width: 129px; height: 126px; margin: 0 0 4px 16px; border: 1px solid var(--frame);
    background: radial-gradient(circle at 50% 38%, #8a8a8a 0%, #5e5e5e 45%, #d8d8d8 100%); }
  .author-text { padding-top: 52px; }
  .isbn-box { position: absolute; left: 323px; top: 728px; width: 220px; height: 132px; border: 1px solid var(--frame); }

  .spine { position: absolute; left: 563px; top: 0; width: 73px; height: 906px; background: var(--spine-dark); }

  .front-cover { position: absolute; left: 636px; top: 0; width: 564px; height: 906px; overflow: hidden; }
  .scene { position: absolute; inset: 0;
    background:
      radial-gradient(circle at 68% 48%, #f2f2f2 0%, #cfcfcf 18%, rgba(180,180,180,0) 45%),
      linear-gradient(180deg, #b4b4b4 0%, #bdbdbd 40%, #8e8e8e 60%, #6c6c6c 66%, #d9d9d9 70%, #bcbcbc 85%, #8a8a8a 100%); }
  .wave-lines { position: absolute; left: 0; top: 600px; width: 564px; height: 160px; }
  .wave-lines path { fill: none; stroke-width: 2; stroke-linecap: round; }
  .wave-lines .wave-light { stroke: var(--wave-light); }
  .wave-lines .wave-blue { stroke: var(--wave-blue); }
  .title-band { position: absolute; left: 0; top: 111px; width: 564px; height: 150px; background: var(--navy); overflow: hidden; }
  .band-wave { position: absolute; left: 0; bottom: 0; width: 564px; height: 40px; }
  .band-wave path { fill: none; stroke: var(--wave-blue); stroke-width: 1.5; }
  .brand-name { position: absolute; left: 80px; top: 58px; display: flex; align-items: center; gap: 10px;
    font-size: 30px; color: var(--brand-blue); letter-spacing: 1px; }
  .brand-mark { width: 20px; height: 20px; background: var(--brand-blue); }
  .title-words { position: absolute; left: 368px; top: 24px; font-family: "Lobster", cursive; font-size: 29px; line-height: 41px; color: var(--cream); }
  .subtitle { position: absolute; right: 80px; top: 279px; width: 300px; text-align: right; font-size: 17.6px; font-weight: 400; line-height: 20.5px; color: #333; }
  .author-band { position: absolute; left: 184px; top: 762px; width: 380px; height: 50px;
    background: linear-gradient(90deg, rgba(41,54,66,0) 0%, var(--navy) 14%, var(--navy) 100%); }
  .author-name { position: absolute; right: 80px; top: 773px; font-size: 20px; font-weight: 400; color: var(--cream); }
</style>
</head>
<body>
<div class="cover">
  <section class="back-cover">
    <h2 class="section-heading summary-heading">Book Summary</h2>
    <p class="summary-text">Believe in you. Trust in You. Rest. Build. Thrive. is a book committed to you. Behavior change and improved health can be challenging. You must feel empowered to make decisions and changes create momentum in the right direction. But, you may not always have the knowledge to do that. This book provides you with practical and fun tools and tips to improve your nutrition, motivation to move, and mindset. You are awesome. You are beautiful. You have the power to control your destiny and future. All you have to do is Rest, Build, and Thrive!</p>

    <h2 class="section-heading author-heading">About the Author</h2>
    <div class="author-block">
      <div class="author-photo" role="img" aria-label="Portrait photo of the author"></div>
      <p class="author-text">Gregory Halvorsen is a Registered Dietitian and Certified Personal Trainer from Cleveland, OH. He graduated from the Westbrook Valley University and currently works as a health coach in the healthcare industry. His passions are fitness, nutrition, science, and motivation. He has extensive knowledge and experience in wellness, healthcare, and disease treatment and disease. Gregory has worked with hundreds of people through counseling, consulting, and coaching in an effort to make a difference in their long-term health. In his spare time, he enjoys exercising, watching movies, and trying out new foods.</p>
    </div>
    <div class="isbn-box"></div>
  </section>

  <div class="spine"></div>

  <section class="front-cover">
    <div class="scene" role="img" aria-label="Black and white photo of a snowy mountain slope with frosted trees and the sun shining"></div>
    <svg class="wave-lines" viewBox="0 0 564 160" aria-hidden="true">
      <path class="wave-light" d="M0 60 C 70 20, 140 20, 210 60 S 350 100, 420 60 S 530 20, 564 40"/>
      <path class="wave-blue" d="M0 85 C 70 45, 140 45, 210 85 S 350 125, 420 85 S 530 45, 564 65"/>
      <path class="wave-light" d="M0 110 C 70 70, 140 70, 210 110 S 350 150, 420 110 S 530 70, 564 90"/>
    </svg>
    <div class="title-band">
      <svg class="band-wave" viewBox="0 0 564 40" aria-hidden="true">
        <path d="M0 28 C 60 10, 120 10, 180 28 S 300 46, 360 28 S 480 10, 564 24"/>
      </svg>
      <div class="brand-name"><span class="brand-mark"></span>Kestrel Press</div>
      <div class="title-words">REST<br>BUILD<br>THRIVE</div>
    </div>
    <h1 class="subtitle">REST. BUILD. THRIVE : A Hands-On Diet, Drive to Act, and Attitude Handbook Building Energy Toward Stronger Vitality &amp; Balance</h1>
    <div class="author-band"></div>
    <p class="author-name">Gregory Halvorsen RD, CPT</p>
  </section>
</div>
</body>
</html>
```